Mobile Recording Studio needs business cards

Open to seeing a creative design, but I want to emphasis my logo and minimize the name/title and company information. Possible a fully black background on card.

My company is a mobile sound recording studio. ok to include a my trailer (actual or cartoon) on the card. My initial thought is more straight forward, but a good design will win me over.

SPECS:
CMYK color mode
High (300ppi) raster effect.
cover bleed area
please deliver: Illustrator file with layers and a pdf at completion.

Name and info for the business card:

Dallin Perry
ADR Mixer

email: Dallin@MixVault.com

address:
248 - 5170 East Hollister
Vancouver, BC V5R 2J4

phone:
604.518.2093 office

website:
www.MixVault.com

FB: @MixVault

Instagram: @TheMixVault

Industry/Entity Type

Television Production

Contact Information for Business Card

Dallin Perry
ADR Mixer

email: Dallin@MixVault.com

address:
248 - 5170 East Hollister
Vancouver, BC V5R 2J4

phone:
604.518.2093 office

website:
www.MixVault.com

FB: @MixVault

Instagram: @TheMixVault

Colors

Designer to choose colors to be used in the design.

Requirements
Must have
• emphasis my logo and minimize the name/title and company information.
• SPECS:
• CMYK color mode
• High (300ppi) raster effect.
• cover bleed area
• please deliver: Illustrator file with layers and a pdf at completion.
Nice to have
• maybe include the following:
• all black background or black theme
• my work trailer (actual or cartoon) refer to Instagram: @TheMixVault

```html
<!DOCTYPE html>
<html lang="en">
<head>
<meta charset="utf-8">
<title>MixVault Business Cards</title>
<link href="https://fonts.googleapis.com/css2?family=Lato:wght@400;700;900&display=swap" rel="stylesheet">
<style>
  :root {
    --backdrop: #2a2a2c;
    --card: #0c0c0d;
    --card-top: #141415;
    --silver: #c9c9cb;
    --silver-dim: #8e8e90;
    --text-muted: #7a7a7c;
    --edge-light: #d8d8da;
    --edge-dark: #6a6a6c;
  }
  * { margin: 0; padding: 0; box-sizing: border-box; }
  html, body {
    width: 1200px;
    height: 900px;
    overflow: hidden;
    background: var(--backdrop);
    font-family: "Lato", sans-serif;
  }
  .stage {
    position: relative;
    width: 1200px;
    height: 900px;
  }
  .card {
    position: absolute;
    left: 320px;
    width: 560px;
    height: 320px;
    background: linear-gradient(160deg, var(--card-top), var(--card) 60%);
    overflow: hidden;
  }
  .card::after {
    content: "";
    position: absolute;
    left: 0; right: 0; bottom: 0;
    height: 4px;
    background: linear-gradient(90deg, var(--edge-dark), var(--edge-light) 40%, var(--edge-dark) 75%, var(--edge-light));
  }
  .card--front { top: 90px; }
  .card--back { top: 480px; }

  .brand-name {
    color: var(--silver);
    font-family: "Lato", sans-serif;
    font-weight: 900;
    letter-spacing: 1px;
    line-height: 1;
  }
  .card--front .brand-name {
    position: absolute;
    top: 95px;
    left: 0; right: 0;
    text-align: center;
    font-size: 76px;
  }
  .socials {
    position: absolute;
    top: 225px;
    left: 0; right: 0;
    display: flex;
    justify-content: center;
    gap: 34px;
    font-size: 15px;
    color: var(--text-muted);
  }
  .social {
    display: flex;
    align-items: center;
    gap: 7px;
  }
  .social__dot {
    width: 14px; height: 14px;
    border-radius: 50%;
    background: var(--silver-dim);
  }

  .team {
    position: absolute;
    top: 34px;
    left: 38px;
  }
  .member + .member { margin-top: 12px; }
  .member__name {
    font-weight: 700;
    font-size: 17px;
    color: var(--silver-dim);
    text-transform: uppercase;
    letter-spacing: .3px;
  }
  .member__role {
    font-size: 13px;
    color: var(--text-muted);
    line-height: 1.3;
  }
  .contact {
    position: absolute;
    left: 38px;
    bottom: 48px;
    font-size: 14px;
    color: var(--text-muted);
  }
  .contact__line {
    display: flex;
    align-items: center;
    gap: 6px;
    line-height: 1.6;
  }
  .contact__icon { width: 12px; height: 12px; flex: none; }
  .card--back .brand-name {
    position: absolute;
    top: 120px;
    right: 50px;
    font-size: 54px;
  }
  .address {
    position: absolute;
    right: 40px;
    bottom: 34px;
    text-align: right;
    font-size: 15px;
    color: var(--text-muted);
    line-height: 1.35;
  }
</style>
</head>
<body>
<main class="stage">
  <section class="card card--front">
    <div class="brand-name">MixVault</div>
    <div class="socials">
      <span class="social"><span class="social__dot"></span>@MixVault</span>
      <span class="social"><span class="social__dot"></span>@TheMixVault</span>
    </div>
  </section>

  <section class="card card--back">
    <div class="team">
      <div class="member">
        <div class="member__name">Dallin Perry</div>
        <div class="member__role">ADR Mixer</div>
      </div>
      <div class="member">
        <div class="member__name">Reid Halvorsen</div>
        <div class="member__role">Engineer</div>
        <div class="member__role">Director of Operations</div>
      </div>
    </div>

    <div class="contact">
      <div class="contact__line">
        <svg class="contact__icon" viewBox="0 0 12 12" aria-hidden="true">
          <path d="M2.5 1 L4.5 1 L5.2 3.4 L4 4.4 C4.6 5.8 6.2 7.4 7.6 8 L8.6 6.8 L11 7.5 L11 9.5 C11 10.3 10.3 11 9.5 11 C5 11 1 7 1 2.5 C1 1.7 1.7 1 2.5 1 Z" fill="#8e8e90"/>
        </svg>
        604.518.2093
      </div>
      <div class="contact__line">
        <svg class="contact__icon" viewBox="0 0 12 12" aria-hidden="true">
          <circle cx="6" cy="6" r="5" fill="none" stroke="#8e8e90" stroke-width="1.2"/>
          <ellipse cx="6" cy="6" rx="2.2" ry="5" fill="none" stroke="#8e8e90" stroke-width="1"/>
          <line x1="1" y1="6" x2="11" y2="6" stroke="#8e8e90" stroke-width="1"/>
        </svg>
        www.MixVault.com
      </div>
    </div>

    <div class="brand-name">MixVault</div>

    <div class="address">
      248 - 5170 East Hollister<br>
      Vancouver, BC V5R 2J4
    </div>
  </section>
</main>
</body>
</html>
```